We need branding for "Velmora" luxury olive oil - 12/02/2022 03:22 EST

Velmora" is new brand of luxury olive oil. We need logo, bottle design and corporate stationary created.

We would like to more focus on the logo and bottle design. I have attached the specification for bottles that will have print on them.

The term “Velmora” is specific for the Mediteran region of Priimošten and it represents the parts of the former vineyards of Well known Darvuk vine, which were literally planted in scarce, Rocky soil. Today, the days of vineyards are far behind us. Vine was long ago replaced with Olive groves on that same, scarce, Rocky soil. Primošten is also Well known for its dry climate which was described long time ago, dating back in Roman ages. Scarce, Rocky soil and dry climate enable the production of healthy Olive fruits with the unique taste, aroma and texture. ALL of our olive groves are maintained only by donkeys, the forgotten symbol of Primošten, The man’s best friend for hundreds of Years in the region of Dalmatia, enabling the 100 % ecological production of olives and preservation of tradition, which we are very proud of. Since ours Olive groves Are placed only on hilly, inaccessible terrain, carved in stones, picking olives can be done only by hand, resulting in the best quality.

We will print our package design on bottles:
- 0,1l small bottles that will used as gifts
- 0,5l bottles
- 0,75 l bottles
Send us ideas with bottles that can used for our brand and please send us link where we can order them and stay in 1 $ max per bottle range.

Here are some brands that we like. Logo and packaging:
- https://www.quorv7-7.com/en/
- https://www.zentalek.com/en/producto/ze-buy-extra-virgin-olive-oil-organic-premium-500-ml-box/
- https://plumfexstudio.com/branding-and-packaging-for-greek-extra-virgin-olive-oil/

```html
<!DOCTYPE html>
<html lang="en">
<head>
<meta charset="utf-8">
<title>Velmora — Extra Virgin Olive Oil Bottle Range</title>
<link rel="stylesheet" href="https://fonts.googleapis.com/css2?family=Fraunces:opsz,wght@9..144,600&family=Montserrat:wght@400;600&display=swap">
<style>
  :root {
    --backdrop: #efefef;
    --glass-black: #0b0b0c;
    --glass-black-sheen: #1c1c1e;
    --glass-olive: #4b5322;
    --glass-olive-deep: #2c3311;
    --ceramic-white: #f6f6f5;
    --ceramic-shade: #e4e4e2;
    --cork-light: #dcbd8f;
    --cork-dark: #8b7661;
    --pattern-dark: #2a2a2b;
    --pattern-olive: #5a6230;
    --pattern-white: #e2e2e0;
    --gold: #c6a263;
    --ink: #1f1f1f;
    --ink-soft: #6d6d6d;
  }
  * { margin: 0; padding: 0; box-sizing: border-box; }
  html, body { width: 1200px; height: 2767px; overflow: hidden; background: var(--backdrop); }
  .canvas { position: relative; width: 1200px; height: 2767px; }
  .bottles { position: absolute; inset: 0; }

  .label {
    position: absolute;
    transform: translateX(-50%);
    display: flex; flex-direction: column; align-items: center;
    color: var(--gold);
    font-family: "Montserrat", sans-serif;
    text-transform: uppercase;
    text-align: center;
    white-space: nowrap;
  }
  .label--ink { color: var(--ink); }
  .label__brand {
    font-family: "Fraunces", serif;
    font-weight: 600;
    text-transform: none;
    line-height: 1;
    letter-spacing: 0.5px;
  }
  .label__rule { height: 1px; background: currentColor; opacity: 0.8; }
  .label__type { letter-spacing: 3px; font-weight: 400; line-height: 1.25; }
  .label__oil { letter-spacing: 3px; font-weight: 600; line-height: 1.25; }
  .label__origin { letter-spacing: 2px; font-weight: 400; line-height: 1.4; }
  .label__dot { width: 3px; height: 3px; border-radius: 50%; background: currentColor; }
  .label__volume { text-transform: none; letter-spacing: 0.5px; }

  .label--large { top: 982px; left: 602px; }
  .label--large .label__brand { font-size: 60px; }
  .label--large .label__rule { width: 150px; margin: 16px 0 22px; }
  .label--large .label__type,
  .label--large .label__oil { font-size: 17px; }
  .label--large .label__origin { font-size: 14px; color: var(--gold); opacity: .85; margin-top: 2px; }
  .label--large .label__dot { margin: 10px 0 8px; }
  .label--large .label__volume { font-size: 14px; }

  .label--small { top: 2292px; }
  .label--small .label__brand { font-size: 44px; }
  .label--small .label__rule { width: 124px; margin: 12px 0 14px; }
  .label--small .label__type,
  .label--small .label__oil { font-size: 13px; }
  .label--small .label__origin { font-size: 10.5px; opacity: .85; }
  .label--small .label__dot { margin: 7px 0 6px; width: 2.5px; height: 2.5px; }
  .label--small .label__volume { font-size: 11px; }
  .label--ink .label__type,
  .label--ink .label__origin { color: var(--ink-soft); }
  .label--left { left: 283px; }
  .label--middle { left: 604px; }
  .label--right { left: 925px; }
</style>
</head>
<body>
<main class="canvas">
  <svg class="bottles" width="1200" height="2767" viewBox="0 0 1200 2767" xmlns="http://www.w3.org/2000/svg">
    <defs>
      <linearGradient id="black-glass" x1="0" x2="1">
        <stop offset="0" stop-color="#050505"/>
        <stop offset="0.25" stop-color="#1c1c1e"/>
        <stop offset="0.6" stop-color="#0b0b0c"/>
        <stop offset="1" stop-color="#050505"/>
      </linearGradient>
      <linearGradient id="olive-glass" x1="0" x2="1">
        <stop offset="0" stop-color="#2c3311"/>
        <stop offset="0.35" stop-color="#4b5322"/>
        <stop offset="1" stop-color="#2c3311"/>
      </linearGradient>
      <linearGradient id="white-ceramic" x1="0" x2="1">
        <stop offset="0" stop-color="#e8e8e6"/>
        <stop offset="0.4" stop-color="#f8f8f7"/>
        <stop offset="1" stop-color="#e4e4e2"/>
      </linearGradient>
      <clipPath id="clip-tall-black">
        <path d="M223,1400 L340,1400 L340,1640 C340,1720 441,1760 441,1870 L441,2480 C441,2520 425,2530 420,2561 L147,2561 C142,2530 126,2520 126,2480 L126,1870 C126,1760 223,1720 223,1640 Z"/>
      </clipPath>
      <clipPath id="clip-olive">
        <path d="M531,1420 L675,1420 L675,1600 C675,1640 724,1640 724,1680 L724,2540 Q724,2555 709,2555 L498,2555 Q483,2555 483,2540 L483,1680 C483,1640 531,1640 531,1600 Z"/>
      </clipPath>
      <clipPath id="clip-white">
        <path d="M857,1460 L990,1460 L990,1650 C990,1690 1071,1690 1071,1740 L1071,2533 Q1071,2548 1056,2548 L794,2548 Q779,2548 779,2533 L779,1740 C779,1690 857,1690 857,1650 Z"/>
      </clipPath>
    </defs>

    <!-- 500 ml flask -->
    <g class="bottle bottle--flask">
      <rect class="bottle__cork" x="512" y="147" width="179" height="76" rx="8" fill="var(--cork-light)"/>
      <rect class="bottle__neck" x="483" y="219" width="206" height="165" rx="6" fill="var(--glass-black)"/>
      <rect class="bottle__body" x="350" y="377" width="504" height="891" rx="26" fill="url(#black-glass)"/>
      <rect class="bottle__print" x="350" y="442" width="504" height="351" fill="var(--pattern-dark)" opacity="0.75" role="img" aria-label="Repeating diamond pattern of olive leaves and drops printed around the shoulder"/>
    </g>

    <!-- 750 ml tall black bottle -->
    <g class="bottle bottle--tall-black">
      <rect class="bottle__cap" x="219" y="1378" width="125" height="40" rx="10" fill="#050505"/>
      <path class="bottle__body" d="M223,1400 L340,1400 L340,1640 C340,1720 441,1760 441,1870 L441,2480 C441,2520 425,2530 420,2561 L147,2561 C142,2530 126,2520 126,2480 L126,1870 C126,1760 223,1720 223,1640 Z" fill="url(#black-glass)"/>
      <rect class="bottle__print" clip-path="url(#clip-tall-black)" x="120" y="1731" width="330" height="312" fill="var(--pattern-dark)" opacity="0.8" role="img" aria-label="Repeating diamond pattern of olive leaves and drops printed on the upper body"/>
    </g>

    <!-- 750 ml olive glass bottle -->
    <g class="bottle bottle--olive">
      <path class="bottle__body" d="M531,1420 L675,1420 L675,1600 C675,1640 724,1640 724,1680 L724,2540 Q724,2555 709,2555 L498,2555 Q483,2555 483,2540 L483,1680 C483,1640 531,1640 531,1600 Z" fill="url(#olive-glass)"/>
      <rect class="bottle__capsule" clip-path="url(#clip-olive)" x="480" y="1406" width="250" height="208" fill="var(--glass-black)"/>
      <rect class="bottle__cap" x="529" y="1406" width="148" height="92" rx="6" fill="#0a0a0a"/>
      <rect class="bottle__print" clip-path="url(#clip-olive)" x="480" y="1731" width="250" height="312" fill="var(--pattern-olive)" opacity="0.6" role="img" aria-label="Repeating diamond pattern of olive leaves and drops printed on the upper body"/>
    </g>

    <!-- 750 ml white ceramic bottle -->
    <g class="bottle bottle--white">
      <path class="bottle__body" d="M857,1460 L990,1460 L990,1650 C990,1690 1071,1690 1071,1740 L1071,2533 Q1071,2548 1056,2548 L794,2548 Q779,2548 779,2533 L779,1740 C779,1690 857,1690 857,1650 Z" fill="url(#white-ceramic)"/>
      <rect class="bottle__cork" x="863" y="1406" width="120" height="60" rx="8" fill="var(--cork-dark)"/>
      <rect class="bottle__print" clip-path="url(#clip-white)" x="775" y="1692" width="300" height="413" fill="var(--pattern-white)" role="img" aria-label="Repeating diamond pattern of olive leaves and drops printed white on white around the shoulder"/>
    </g>
  </svg>

  <div class="label label--large">
    <span class="label__brand">Velmora</span>
    <span class="label__rule"></span>
    <span class="label__type">Extra Virgin</span>
    <span class="label__oil">Olive Oil</span>
    <span class="label__origin">Made in Priimoštenr</span>
    <span class="label__dot"></span>
    <span class="label__volume">500ml</span>
  </div>

  <div class="label label--small label--left">
    <span class="label__brand">Velmora</span>
    <span class="label__rule"></span>
    <span class="label__type">Extra Virgin</span>
    <span class="label__oil">Olive Oil</span>
    <span class="label__origin">Made in Priimoštenr</span>
    <span class="label__dot"></span>
    <span class="label__volume">750ml</span>
  </div>

  <div class="label label--small label--middle">
    <span class="label__brand">Velmora</span>
    <span class="label__rule"></span>
    <span class="label__type">Extra Virgin</span>
    <span class="label__oil">Olive Oil</span>
    <span class="label__origin">Made in Priimoštenr</span>
    <span class="label__dot"></span>
    <span class="label__volume">750ml</span>
  </div>

  <div class="label label--small label--right label--ink">
    <span class="label__brand">Velmora</span>
    <span class="label__rule"></span>
    <span class="label__type">Extra Virgin</span>
    <span class="label__oil">Olive Oil</span>
    <span class="label__origin">Made in Priimoštenr</span>
    <span class="label__dot"></span>
    <span class="label__volume">750ml</span>
  </div>
</main>
</body>
</html>
```